Bright Lantern Way (BLWY) Business Card - company with a mission

Note* The file attached... orange with "Bright Lantern WAY" (in CAPS) is our logo. I am also open to having the text "bright lantern way" OUTSIDE the orange round logo for business card (so yes, you may take the text out).

The info: (the following info are separate. So either you can use Marcus or Renata for now, but that will be 2 separate cards, not together in one card. Thanks!!

Marcus T Delvin
202.555.0137
marcus@brightlanternway.example
Managing Partner

Renata P Osk
202.555.0184
renata@brightlanternway.example
Managing Partner

Our website: www.brightlanternway.example

BLWY LLC stands for Bright Lantern Way (non profit arm is called lantern glow foundation)—our business is based out of New York City and has a non-profit arm where for every bar of soap you purchase, we donate a bar (don’t want any designs that limits us to only soap). Currently working with South Africa. We want the focus to be organic/natural soap with a mission.

Looking for a clean, fresh design.

Industry/Entity Type

Non-Profit

Requirements
Must have
• Clean, fresh, refreshing. Design should not be too busy.

```html
<!DOCTYPE html>
<html lang="en">
<head>
<meta charset="utf-8">
<title>Bright Lantern Way — Business Card</title>
<link rel="stylesheet" href="https://fonts.googleapis.com/css2?family=Open+Sans:wght@400;600&display=swap">
<style>
  :root {
    --bg: #e9e6e2;
    --card: #343434;
    --band: #4a4a4a;
    --band-dark: #2a2a2a;
    --orange: #f5a26a;
    --text: #f2f2f2;
    --muted: #cfcfcf;
  }
  * { margin: 0; padding: 0; box-sizing: border-box; }
  html, body { width: 1200px; height: 621px; overflow: hidden; }
  body {
    background: var(--bg);
    font-family: "Open Sans", Arial, sans-serif;
    position: relative;
  }
  .card {
    position: absolute;
    top: 161px;
    width: 520px;
    height: 298px;
    background: var(--card);
    border-radius: 4px;
    box-shadow: 0 6px 18px rgba(0,0,0,.25);
    overflow: hidden;
    color: var(--text);
  }
  .card--front { left: 50px; }
  .card--back { left: 630px; }

  .corner-mark { position: absolute; left: 0; top: 0; }

  .holder { position: absolute; left: 40px; top: 78px; }
  .holder__name { color: var(--orange); font-size: 19px; font-weight: 400; }
  .holder__title { color: var(--text); font-size: 12px; margin-top: 2px; }

  .brand { position: absolute; display: flex; align-items: center; gap: 12px; }
  .brand__dot { border-radius: 50%; background: var(--orange); flex: none; }
  .brand__name { font-weight: 600; color: var(--text); letter-spacing: .2px; }

  .card--front .brand { left: 214px; top: 150px; }
  .card--front .brand__dot { width: 54px; height: 54px; }
  .card--front .brand__name { font-size: 21px; }

  .contacts { position: absolute; left: 256px; top: 218px; list-style: none; }
  .contacts li { display: flex; align-items: center; gap: 8px; font-size: 11.5px; color: var(--muted); line-height: 19px; }
  .contacts svg { width: 11px; height: 11px; flex: none; }

  .card--back .brand { left: 140px; top: 104px; }
  .card--back .brand__dot { width: 66px; height: 66px; }
  .card--back .brand__name { font-size: 22px; }

  .back-band { position: absolute; left: 0; right: 0; bottom: 22px; height: 14px; background: var(--band); }
  .back-band::after { content: ""; position: absolute; left: 0; right: 0; bottom: -6px; height: 6px; background: var(--band-dark); }
  .back-site { position: absolute; left: 150px; bottom: 44px; font-size: 11px; color: var(--orange); }
</style>
</head>
<body>

<section class="card card--front" aria-label="Business card front">
  <svg class="corner-mark" width="130" height="80" viewBox="0 0 130 80" aria-hidden="true">
    <polygon points="0,0 130,0 84,58 46,58 0,20" fill="var(--band)"/>
    <polygon points="30,0 100,0 65,44" fill="var(--orange)"/>
  </svg>

  <div class="holder">
    <p class="holder__name">Marcus T Delvin</p>
    <p class="holder__title">Managing Partner</p>
  </div>

  <div class="brand">
    <span class="brand__dot"></span>
    <span class="brand__name">brightlanternway</span>
  </div>

  <ul class="contacts">
    <li>
      <svg viewBox="0 0 12 12" aria-hidden="true"><circle cx="6" cy="6" r="6" fill="var(--orange)"/><path d="M4 3.2c.5 2.3 1.9 4 4.2 5l.6-1-1.2-.6-.5.5c-.8-.4-1.5-1.1-1.9-2l.5-.5L5 3.3z" fill="var(--card)"/></svg>
      202.555.0137
    </li>
    <li>
      <svg viewBox="0 0 12 12" aria-hidden="true"><rect x="0" y="1.5" width="12" height="9" rx="1.5" fill="var(--orange)"/><path d="M1.5 3l4.5 3.5L10.5 3" stroke="var(--card)" fill="none"/></svg>
      marcus@brightlanternway.example
    </li>
    <li>
      <svg viewBox="0 0 12 12" aria-hidden="true"><circle cx="6" cy="6" r="6" fill="var(--orange)"/><path d="M0.5 6h11M6 .5c-2.5 3-2.5 8 0 11M6 .5c2.5 3 2.5 8 0 11" stroke="var(--card)" stroke-width=".8" fill="none"/></svg>
      www.brightlanternway.example
    </li>
  </ul>
</section>

<section class="card card--back" aria-label="Business card back">
  <div class="brand">
    <span class="brand__dot"></span>
    <span class="brand__name">brightlanternway</span>
  </div>
  <p class="back-site">www.brightlanternway.example</p>
  <div class="back-band"></div>
</section>

</body>
</html>
```